Daily Paid Subscription Newsletter

We need a newsletter design, the details of which are:
What are we doing: We are launching a new paid subscription service targeting marketers, social media agaencies and online publishers.
What will the newsletter content be like: This will contain "content ideas" brands and publishers can use
What is the frequency of the newsletter: This will be a daily newsletter. Not on weekends
Is there a construct of sorts: Yes. There are 3 components to the newsletter. (1) Whats trending today / Hot Today (2) Whats Trending this week / Hot this week and (3) Seasonal Trends / Hot this month
What media formats we need to consider: Text, Images and Videos
What is the name of this newsletter: Plover Suggests (please help in creating this unit with the help of attached logo)
What is being uploaded: (1) A sample day's content for the newsletter in a word doc. Refer to "Plover Suggests Sample & Brief.doc"
(2) Plover logo
Target Market(s)
Social Media Agencies, marketers, publishers. Global market
Industry/Entity Type
Marketing
Font styles to use
Colors
Designer to choose colors to be used in the design.
Requirements
Must have
- more text, less visual. this is a paid subscription service. Many stories upfront
Nice to have
- hues of the website. this is WIP but you can refer to plover-hub.co.in to know more
Should not have
- avoid going beyod 2 or max 3 scrolls

```html
<!DOCTYPE html>
<html lang="en">
<head>
<meta charset="utf-8">
<title>Plover Suggests – Hot Today</title>
<link rel="stylesheet" href="https://fonts.googleapis.com/css2?family=Open+Sans:wght@400;600&family=Ubuntu:wght@300;700&display=swap">
<style>
  :root {
    --header-bg: #231f20;
    --band-red: #d7191f;
    --topic-orange: #f47a20;
    --link-grey: #9a9a9a;
    --underline-grey: #c4c4c4;
    --tag-grey: #a3a3a3;
    --footer-bg: #2b2b2b;
    --footer-text: #b0b0b0;
    --white: #ffffff;
    --brand-dot: #6cc4e8;
  }
  * { margin: 0; padding: 0; box-sizing: border-box; }
  html, body { width: 1200px; height: 2277px; overflow: hidden; background: var(--white); }
  body { position: relative; font-family: "Open Sans", Arial, sans-serif; }

  .masthead {
    position: absolute; left: 0; top: 0; width: 1200px; height: 314px;
    background: var(--header-bg);
  }
  .brand-mark { position: absolute; left: 532px; top: 36px; }
  .brand-name {
    position: absolute; left: 0; width: 1200px; top: 186px;
    text-align: center; color: var(--white);
    font-family: "Ubuntu", Arial, sans-serif;
    font-weight: 300; font-size: 52px; line-height: 60px; letter-spacing: 0.5px;
  }

  .edition-band {
    position: absolute; left: 0; top: 314px; width: 1200px; height: 113px;
    background: var(--band-red); color: var(--white);
    font-family: "Ubuntu", Arial, sans-serif; font-weight: 700;
    font-size: 41px; line-height: 113px; text-align: center;
  }

  .topic { position: absolute; }
  .topic--col-left { left: 86px; width: 425px; }
  .topic--col-right { left: 672px; width: 440px; }
  .topic--row-1 { top: 505px; }
  .topic--row-2 { top: 1221px; }

  .topic-title {
    color: var(--topic-orange);
    font-family: "Ubuntu", Arial, sans-serif; font-weight: 700;
    font-size: 31px; line-height: 43px;
  }
  .story-list { list-style: none; margin-top: 20px; }
  .story { margin-bottom: 41px; }
  .story-link {
    color: var(--link-grey); font-weight: 600;
    font-size: 27px; line-height: 34px; text-decoration: underline;
    text-decoration-color: var(--underline-grey); text-decoration-thickness: 2px;
    text-underline-offset: 5px;
  }
  .story-tags {
    display: block; margin-top: 4px;
    color: var(--tag-grey); font-size: 19px; line-height: 24px;
    text-transform: uppercase;
  }

  .site-footer {
    position: absolute; left: 0; top: 2170px; width: 1200px; height: 107px;
    background: var(--footer-bg); color: var(--footer-text);
    font-size: 22px; line-height: 107px; text-align: center;
  }
</style>
</head>
<body>
  <header class="masthead">
    <svg class="brand-mark" width="136" height="136" viewBox="0 0 136 136" aria-hidden="true">
      <circle cx="68" cy="68" r="58" fill="var(--brand-dot)"/>
    </svg>
    <div class="brand-name">plover suggests</div>
  </header>

  <div class="edition-band">Hot Today</div>

  <section class="topic topic--col-left topic--row-1">
    <h2 class="topic-title">Trending Topic: Fake cash dispensed from NBR ATM</h2>
    <ul class="story-list">
      <li class="story"><a class="story-link">Guide to identifying real notes</a><span class="story-tags">Mobile / Finance</span></li>
      <li class="story"><a class="story-link">What to do if you find yourself with fake cash</a><span class="story-tags">Mobile / Job Sites</span></li>
      <li class="story"><a class="story-link">Yet another reason to go cashless</a><span class="story-tags">Job Sites / Education</span></li>
    </ul>
  </section>

  <section class="topic topic--col-right topic--row-1">
    <h2 class="topic-title">Trending Topic: Ultra man- Arjun Valekar</h2>
    <ul class="story-list">
      <li class="story"><a class="story-link">10 things to do with your money instead of RV tickets</a><span class="story-tags">Bikes / F&amp;B</span></li>
      <li class="story"><a class="story-link">How to save up for the next big bang concert</a><span class="story-tags">F&amp;B / Pharma / Batteries</span></li>
      <li class="story"><a class="story-link">Think about the long run</a><span class="story-tags">Finance</span></li>
      <li class="story"><a class="story-link">What to wear to the RV concert</a><span class="story-tags">F&amp;B / Pharma / Batteries</span></li>
    </ul>
  </section>

  <section class="topic topic--col-left topic--row-2">
    <h2 class="topic-title">Lay offs in Dealnest</h2>
    <ul class="story-list">
      <li class="story"><a class="story-link">Apps to monitor money spending</a><span class="story-tags">Mobile / Finance</span></li>
      <li class="story"><a class="story-link">How your phone can help you make money</a><span class="story-tags">Mobile / Job Sites</span></li>
      <li class="story"><a class="story-link">Apps that can help you keep updated with jobs</a><span class="story-tags">Job Sites / Education</span></li>
      <li class="story"><a class="story-link">How to spend your sabbatical without feeling jobless</a><span class="story-tags">Travel / Job Sites</span></li>
      <li class="story"><a class="story-link">Can't afford new clothes? Try these DIY Hacks</a><span class="story-tags">E-Commerce / Lifestyle / Retail</span></li>
      <li class="story"><a class="story-link">How to look sharp at your next interview</a><span class="story-tags">Job Sites / Retail</span></li>
    </ul>
  </section>

  <section class="topic topic--col-right topic--row-2">
    <h2 class="topic-title">Trending Topic: Ultra man- Arjun Valekar</h2>
    <ul class="story-list">
      <li class="story"><a class="story-link">Arjun Valekar asks #WhyStopHere</a><span class="story-tags">Bikes / F&amp;B</span></li>
      <li class="story"><a class="story-link">Running till the end</a><span class="story-tags">F&amp;B / Pharma / Batteries</span></li>
      <li class="story"><a class="story-link">Think about the long run</a><span class="story-tags">Finance</span></li>
      <li class="story"><a class="story-link">Healthy food is the first step to running a marathon</a><span class="story-tags">F&amp;B / Sport Equipment</span></li>
      <li class="story"><a class="story-link">Make things last longer</a><span class="story-tags">Batteries / Home Improvement</span></li>
    </ul>
  </section>

  <footer class="site-footer">Copyright 2016-2017 Helix Media Pvt. Ltd.</footer>
</body>
</html>
```